Broschüre
Zielgruppe
Die K.O.R.N. Valor Domus GmbH ist ein inhabergeführtes Immobilienunternehmen mit Sitz in Moers. Wir sind spezialisiert auf den direkten Ankauf von Mehrfamilienhäusern, Wohnanlagen und größeren Wohnimmobilien in Nordrhein-Westfalen. Unser Schwerpunkt liegt auf einer schnellen, diskreten und unbürokratischen Abwicklung – vom ersten Kontakt bis zum notariellen Abschluss. Wir kaufen Objekte in jedem Zustand, ob vermietet, leerstehend oder sanierungsbedürftig.
Wer ist Deine Zielgruppe?
• Institutionelle Eigentümer z.b. Wohnungsunternehmen und Investoren, die Bestände veräußern wollen
Aufgabenstellung
• Corporate Identity: Seriös, modern, vertrauenswürdig. Die Broschüre soll unsere Professionalität und Diskretion betonen.
• Farben: Anlehnung an die Unternehmensfarben der K.O.R.N. Valor Domus GmbH (dezent, elegant, z. B. dunkles Blau, Grau, Weiß; ggf. Akzentfarbe Gold oder ein warmes Gelb).
• Schriftarten: Gut lesbar, modern, ohne verschnörkelte Fonts.
• Format: Hochformat DIN A4, 4–8 Seiten, übersichtlich und klar strukturiert.
• Bildsprache: Hochwertige Immobilienbilder, urbane Aufnahmen aus NRW, Detailfotos (z. B. Architektur, Gebäudeansichten) sowie emotionale Motive, die Vertrauen und Sicherheit vermitteln.
• Ton & Stil: Seriös, diskret, aber sympathisch – nicht zu werblich, sondern lösungsorientiert.
• Logo: Unser Firmenlogo muss auf dem Titel und der Rückseite gut sichtbar platziert sein.

```html
<!DOCTYPE html>
<html lang="de">
<head>
<meta charset="utf-8">
<title>Valor Domus – Broschüre Titel</title>
<link rel="stylesheet" href="https://fonts.googleapis.com/css2?family=Gelasio:ital,wght@0,400;1,400&family=Raleway:wght@300;400;500&display=swap">
<style>
  :root {
    --stage: #dcdcdc;
    --navy-deep: #141f45;
    --navy-light: #34446f;
    --blue-strong: #124ea3;
    --blue-soft: #3a7cc0;
    --band: #3b4873;
    --paper: #ffffff;
    --tag-bg: #eeeeef;
    --tag-ink: #1b2447;
    --text-muted: #c3c8d8;
  }
  html, body {
    margin: 0;
    width: 1200px;
    height: 1200px;
    overflow: hidden;
    background: var(--stage);
  }
  .cover {
    position: absolute;
    left: 246px;
    top: 100px;
    width: 707px;
    height: 1000px;
    background: linear-gradient(160deg, var(--navy-deep) 0%, #1b2851 45%, var(--navy-light) 100%);
    box-shadow: 0 18px 40px rgba(0,0,0,0.25);
    overflow: hidden;
  }
  .brand-tag {
    position: absolute;
    top: 0;
    left: 50%;
    transform: translateX(-50%);
    width: 190px;
    height: 96px;
    background: var(--tag-bg);
    display: flex;
    align-items: center;
    justify-content: center;
    gap: 10px;
  }
  .brand-dot {
    width: 10px;
    height: 10px;
    border-radius: 50%;
    background: var(--tag-ink);
  }
  .brand-name {
    font-family: "Raleway", sans-serif;
    font-weight: 500;
    font-size: 15px;
    letter-spacing: 0.04em;
    color: var(--tag-ink);
    white-space: nowrap;
  }
  .headline {
    position: absolute;
    top: 172px;
    left: 0;
    right: 0;
    margin: 0;
    text-align: center;
    font-family: "Gelasio", serif;
    font-weight: 400;
    font-size: 46px;
    line-height: 1.15;
    color: var(--paper);
  }
  .headline em { font-style: italic; display: block; }
  .divider {
    position: absolute;
    top: 326px;
    left: 50%;
    width: 270px;
    height: 1px;
    transform: translateX(-50%);
    background: linear-gradient(90deg, rgba(255,255,255,0), rgba(255,255,255,0.8), rgba(255,255,255,0));
  }
  .contact {
    position: absolute;
    top: 358px;
    left: 0;
    right: 0;
    text-align: center;
    font-family: "Raleway", sans-serif;
    font-weight: 300;
    font-size: 13px;
    line-height: 1.55;
    color: var(--text-muted);
  }
  .contact .web {
    margin-top: 14px;
    font-size: 15px;
    font-weight: 400;
    color: var(--paper);
  }
  .geometry {
    position: absolute;
    left: 0;
    top: 0;
    width: 707px;
    height: 1000px;
  }
</style>
</head>
<body>
  <main class="cover">
    <svg class="geometry" viewBox="0 0 707 1000" aria-hidden="true">
      <defs>
        <linearGradient id="blueFade" x1="0" y1="0" x2="1" y2="0">
          <stop offset="0" stop-color="var(--blue-strong)"/>
          <stop offset="1" stop-color="var(--blue-soft)"/>
        </linearGradient>
      </defs>
      <rect class="block-upper" x="0" y="640" width="460" height="120" fill="var(--blue-strong)"/>
      <rect class="block-lower" x="180" y="790" width="527" height="150" fill="url(#blueFade)"/>
      <rect class="foot-band" x="0" y="958" width="707" height="42" fill="var(--band)"/>
    </svg>

    <div class="brand-tag">
      <span class="brand-dot"></span>
      <span class="brand-name">Korn Valor Domus</span>
    </div>

    <h1 class="headline"><em>Wir kaufen</em>Immobilien in NRW.</h1>

    <div class="divider"></div>

    <div class="contact">
      <div>Kastanienweg 8, 45127 Essen</div>
      <div>kontakt@valordomus-immo.de</div>
      <div>0201 7384 215</div>
      <div class="web">www.valordomus-immo.de</div>
    </div>
  </main>
</body>
</html>
```